Certificate of Completion - Educational Trainings

We are looking for a certificate of completion for individuals who complete one of our specific trainings. Files should be provided in a Word (docx) or PowerPoint (pptx) format. The "Halvorcrest example.png" file is to show necessary information. Copies of logos have been included for design purposes.

Target Market(s)

Training Participants

Industry/Entity Type

Healthcare

Font styles to use
Sans Serif

```html
<!DOCTYPE html>
<html lang="en">
<head>
<meta charset="utf-8">
<title>Halvorcrest Certificate of Completion</title>
<link rel="stylesheet" href="https://fonts.googleapis.com/css2?family=Montserrat:wght@800&family=Josefin+Sans:wght@300;400&family=Great+Vibes&family=Roboto+Condensed:wght@400&display=swap">
<style>
  :root {
    --frame-green: #66ad47;
    --ornament-green: #c9e0bd;
    --ornament-line: #8fbf78;
    --paper: #fdfdfb;
    --ink: #151515;
    --muted-ink: #3a3a3a;
    --page-bg: #f2f2f0;
  }
  * { margin: 0; padding: 0; box-sizing: border-box; }
  html, body {
    width: 1200px; height: 800px; overflow: hidden;
    background: var(--page-bg);
  }
  .certificate {
    position: relative;
    width: 1200px; height: 800px;
    background: var(--frame-green);
    font-family: "Josefin Sans", sans-serif;
    color: var(--ink);
  }
  .certificate__mat {
    position: absolute; inset: 16px;
    background: var(--paper);
  }
  .certificate__ornament {
    position: absolute; inset: 30px;
    border: 24px solid var(--ornament-green);
    outline: 1px solid var(--ornament-line);
  }
  .certificate__rule {
    position: absolute; inset: 62px;
    border: 2px solid var(--ornament-line);
  }
  .certificate__body {
    position: absolute; inset: 64px;
    text-align: center;
  }
  .brand {
    position: absolute; top: 14px; left: 0; right: 0;
  }
  .brand__name {
    display: inline-flex; align-items: center; gap: 14px;
    font-family: "Montserrat", sans-serif; font-weight: 800;
    font-size: 40px; line-height: 1; letter-spacing: 1px;
  }
  .brand__dot {
    width: 20px; height: 20px; border-radius: 50%;
    background: var(--frame-green);
  }
  .brand__address {
    margin-top: 6px;
    font-size: 13px; letter-spacing: 1.5px; line-height: 1.3;
    text-transform: uppercase; color: var(--muted-ink);
  }
  .title {
    position: absolute; top: 130px; left: 0; right: 0;
    font-weight: 300; font-size: 96px; letter-spacing: 6px;
    line-height: 1;
  }
  .title__sub {
    position: absolute; top: 214px; left: 0; right: 0;
    font-family: "Great Vibes", cursive; font-size: 40px; line-height: 1.1;
    padding-left: 160px;
  }
  .awarded {
    position: absolute; top: 268px; left: 0; right: 0;
    font-size: 25px; line-height: 1.2; letter-spacing: 2px; text-transform: uppercase;
  }
  .recipient {
    position: absolute; top: 302px; left: 50%; transform: translateX(-50%);
    width: 520px; padding-bottom: 2px;
    border-bottom: 1.5px solid var(--ink);
    font-family: "Great Vibes", cursive; font-size: 44px; line-height: 1.25;
  }
  .course {
    position: absolute; top: 372px; left: 0; right: 0;
    font-size: 21px; letter-spacing: 2px; line-height: 1.28;
    font-variant: small-caps;
  }
  .seal {
    position: absolute; top: 516px; left: 0; right: 0;
    font-family: "Montserrat", sans-serif; font-weight: 800;
    font-size: 24px; line-height: 1.2; letter-spacing: 1px;
  }
  .signoff {
    position: absolute; bottom: 40px;
    width: 300px; text-align: center;
  }
  .signoff--date { left: 70px; }
  .signoff--signature { right: 70px; bottom: 52px; }
  .signoff__value {
    border-bottom: 1.5px solid var(--ink);
    padding-bottom: 4px;
    font-family: "Great Vibes", cursive; font-size: 30px; line-height: 1.2;
  }
  .signoff--date .signoff__value {
    font-family: "Josefin Sans", sans-serif;
    font-weight: 300; font-size: 24px; letter-spacing: 2px; line-height: 1.5;
  }
  .signoff__label {
    margin-top: 8px; font-size: 20px; line-height: 1.2; letter-spacing: 2px;
    text-transform: uppercase;
  }
  .disclaimer {
    position: absolute; bottom: 10px; left: 0; right: 0;
    font-family: "Roboto Condensed", sans-serif; font-size: 13px; line-height: 1.2;
    text-transform: uppercase; letter-spacing: 0.2px;
  }
</style>
</head>
<body>
  <main class="certificate">
    <div class="certificate__mat"></div>
    <div class="certificate__ornament" role="img" aria-label="Fine green guilloche border pattern framing the certificate"></div>
    <div class="certificate__rule"></div>

    <section class="certificate__body">
      <header class="brand">
        <div class="brand__name"><span class="brand__dot"></span>HALVORCREST</div>
        <p class="brand__address">
          48 Larkmoor Lane, Ste.310<br>
          Brenford, ME 04920<br>
          National Council Sponsor Number 51872
        </p>
      </header>

      <h1 class="title">CERTIFICATE</h1>
      <p class="title__sub">of completion</p>

      <p class="awarded">This certificate is awarded to</p>
      <p class="recipient">Marcus Feldhollow</p>

      <p class="course">
        For Successful completion of<br>
        Best Practices : Budget Process/Budget Building<br>
        Completed Online<br>
        Field of Study Finance<br>
        CPE Credits: 1
      </p>

      <div class="seal">HALVORCREST</div>

      <div class="signoff signoff--date">
        <p class="signoff__value">05/16/2024</p>
        <p class="signoff__label">Completion Date</p>
      </div>

      <div class="signoff signoff--signature">
        <p class="signoff__value">Rena Voskil</p>
        <p class="signoff__label">Senior Consultant</p>
      </div>

      <p class="disclaimer">In accordance with the standard of the National Council of Learning Sponsors CPE credits have been granted based on a 50 minute hour</p>
    </section>
  </main>
</body>
</html>
```